The Brivo Agency launch adverisment

The Brivo agency is an on line estate agency aimed at the Spanish market.
The property owners buy space on The Brivo agency site and promote their
property themselves with the help of a professional estate agent.
The attached file has a very rough outline of an ad , the copy is right and in the right order. This rough design is to give you an idea of what we
need to get over.
Also in the file is a number of pictures of the type of properties we want to attract. Rather than have them spread around the page I would like to see a montage of them so that no 1 property is taking the main emphasis.
The packages have been discounted by 100e as the launch offer,which needs to come across. The ad needs to work in A5 and A4 formats.

```html
<!DOCTYPE html>
<html lang="en">
<head>
<meta charset="utf-8">
<title>The Brivo Agency – Launch Packages</title>
<link href="https://fonts.googleapis.com/css2?family=Open+Sans:ital,wght@0,400;0,600;0,700;1,400;1,700;1,800&family=Oswald:wght@400;500&family=Roboto+Condensed:wght@300;400;700&display=swap" rel="stylesheet">
<style>
:root{
  --navy:#0e4a80;
  --navy-dark:#0a3862;
  --blue:#1f6aa8;
  --orange:#ee6a1f;
  --orange-light:#f5892e;
  --yellow:#ffe116;
  --green:#2fae3c;
  --red:#e3202a;
  --row-alt:#eeeff1;
  --row:#ffffff;
  --ink:#222;
  --page-bg:#e9e9e9;
}
*{box-sizing:border-box;margin:0;padding:0}
html,body{width:1200px;height:1200px;overflow:hidden}
body{background:var(--page-bg);font-family:"Open Sans",Arial,sans-serif;position:relative}
.flyer{position:absolute;left:219px;top:43px;width:774px;height:1095px;background:var(--orange);overflow:hidden}

/* header */
.header{position:absolute;left:0;top:0;width:774px;height:125px;background:#fff}
.header-rule{position:absolute;left:0;top:125px;width:774px;height:7px;background:var(--navy)}
.brand{position:absolute;left:22px;top:68px;display:flex;align-items:center;gap:10px}
.brand-dot{width:22px;height:22px;border-radius:50%;background:var(--orange)}
.brand-name{font-family:"Open Sans",sans-serif;font-weight:700;font-size:29px;color:var(--navy);letter-spacing:-.3px}
.launch-banner{position:absolute;left:430px;top:24px;width:344px;height:84px}
.launch-banner svg{position:absolute;inset:0}
.launch-text{position:absolute;left:60px;top:6px;width:270px;text-align:center;color:#fff;font-style:italic;font-weight:700;font-size:25px;line-height:1.45}
.launch-text strong{font-size:33px;font-weight:800}

/* hero */
.hero{position:absolute;left:0;top:134px;width:774px;height:236px}
.photo{position:absolute;top:0;height:236px}
.photo-villa{left:0;width:390px;background:linear-gradient(180deg,#7fb3e0 0%,#d9e6ee 38%,#f2efe6 55%,#3fa8e0 78%,#1d7fc4 100%)}
.photo-tower{left:394px;width:380px;background:linear-gradient(100deg,#a9b6bf 0%,#8a5a45 30%,#c9c3b8 55%,#e4e1da 100%)}
.hero-swoosh{position:absolute;left:0;top:134px;width:774px;height:245px}
.hero-title{position:absolute;left:0;top:318px;width:774px;text-align:center;font-family:"Oswald",sans-serif;font-weight:400;font-size:35px;color:#fff;letter-spacing:-.3px}

/* intro copy */
.intro{position:absolute;left:0;top:384px;width:774px;text-align:center;color:#fff;font-style:italic;font-size:14px}
.intro p{line-height:1.1}
.intro b{font-weight:700;font-size:19px}
.intro .l1{margin-top:2px}
.intro .l2{margin-top:6px}
.intro .l3{margin-top:12px}
.intro .l5{margin-top:10px}

/* packages table */
.packages{position:absolute;left:10px;top:514px;width:754px;font-family:"Roboto Condensed",sans-serif}
.pkg-row{display:grid;grid-template-columns:218px 124px 136px 137px 139px;height:22.4px;align-items:center}
.pkg-row:nth-child(odd){background:var(--row-alt)}
.pkg-row:nth-child(even){background:var(--row)}
.pkg-head{height:33px;background:none!important}
.pkg-head .corner{height:33px;background:linear-gradient(180deg,#fff,#dcdde0)}
.pkg-head .pkg-name{height:33px;background:linear-gradient(180deg,#1a5c98,var(--navy-dark));color:#fff;font-family:"Oswald",sans-serif;font-size:19px;display:flex;align-items:center;justify-content:center;letter-spacing:-.4px;border-left:2px solid #fff}
.feature{font-size:13.5px;color:var(--ink);padding-left:10px;letter-spacing:-.3px;white-space:nowrap}
.mark{display:flex;justify-content:center}
.mark svg{width:14px;height:14px}
.price-row .feature,.price-row .price{color:var(--red);font-size:13.5px;font-weight:300}
.price{text-align:center}
.offer-row{height:26px;background:var(--yellow)!important}
.offer-row .feature{color:var(--red);font-size:13.5px}
.offer-row .price{color:#111;font-weight:700;font-size:15px;border-left:2px solid var(--orange-light)}

/* footer */
.footer{position:absolute;left:0;top:1047px;width:774px;height:48px;background:linear-gradient(180deg,var(--blue),var(--navy-dark));color:#fff;text-align:center;font-size:13.5px;font-weight:600;padding-top:3px;line-height:1.4}
.footer .site{font-size:16px}
</style>
</head>
<body>
<svg width="0" height="0" style="position:absolute" aria-hidden="true">
  <symbol id="tick" viewBox="0 0 14 14"><path d="M1.5 7.2 5.2 10.8 12.5 3.4" fill="none" stroke="#2fae3c" stroke-width="2.6" stroke-linecap="round" stroke-linejoin="round"/></symbol>
  <symbol id="cross" viewBox="0 0 14 14"><path d="M2.5 2.5 11.5 11.5M11.5 2.5 2.5 11.5" fill="none" stroke="#e3202a" stroke-width="2.8" stroke-linecap="round"/></symbol>
</svg>

<div class="flyer">
  <header class="header">
    <div class="brand"><span class="brand-dot"></span><span class="brand-name">The Brivo Agency.com</span></div>
    <div class="launch-banner">
      <svg viewBox="0 0 344 84" width="344" height="84">
        <polygon points="28,0 344,0 344,84 28,84 0,42" fill="#0e4a80"/>
        <polygon points="40,0 50,0 22,42 50,84 40,84 12,42" fill="#fff"/>
      </svg>
      <div class="launch-text">Launches Packages<br>from <strong>€299</strong></div>
    </div>
  </header>
  <div class="header-rule"></div>

  <section class="hero">
    <div class="photo photo-villa" role="img" aria-label="Photo of a white Spanish villa with arches, palm tree and swimming pool"></div>
    <div class="photo photo-tower" role="img" aria-label="Photo of a tall modern apartment block with balconies"></div>
  </section>
  <svg class="hero-swoosh" viewBox="0 0 774 245" width="774" height="245" aria-hidden="true">
    <defs>
      <linearGradient id="swooshBlue" x1="0" y1="0" x2="0" y2="1">
        <stop offset="0" stop-color="#1f6aa8"/><stop offset="1" stop-color="#0a3862"/>
      </linearGradient>
    </defs>
    <path d="M0 205 Q387 125 774 205 L774 245 L0 245 Z" fill="#0e4a80"/>
    <path d="M0 210 Q387 140 774 215 L774 240 L0 240 Z" fill="url(#swooshBlue)"/>
    <path d="M0 198 Q360 100 774 210" fill="none" stroke="#f5892e" stroke-width="5"/>
    <rect x="0" y="236" width="774" height="5" fill="#ffb21a"/>
  </svg>
  <h1 class="hero-title">YOUR ONLINE ESTATE AGENT</h1>

  <section class="intro">
    <p class="l1">98% of properties are first viewed online.</p>
    <p class="l2">The Brivo Agency.com is the cheapest way to sell your home, at <b>0% commission</b></p>
    <p class="l3">The Brivo Agency.com lets <b>you take control</b> of the selling process, so choose from our comprehensive selection<br>of packages and arrange a visit from one of our experienced agents, and get online today.</p>
    <p class="l5">The Brivo Agency.com is the new way to sell property, from as little as <b>little as €299</b></p>
  </section>

  <section class="packages">
    <div class="pkg-row pkg-head"><div class="corner"></div><div class="pkg-name">PACKAGE 1</div><div class="pkg-name">PACKAGE 2</div><div class="pkg-name">PACKAGE 3</div><div class="pkg-name">PACKAGE 4</div></div>
    <div class="pkg-row"><div class="feature">Initial home visit</div><div class="mark"><svg><use href="#tick"/></svg></div><div class="mark"><svg><use href="#tick"/></svg></div><div class="mark"><svg><use href="#tick"/></svg></div><div class="mark"><svg><use href="#tick"/></svg></div></div>
    <div class="pkg-row"><div class="feature">Customised sale board</div><div class="mark"><svg><use href="#tick"/></svg></div><div class="mark"><svg><use href="#tick"/></svg></div><div class="mark"><svg><use href="#tick"/></svg></div><div class="mark"><svg><use href="#tick"/></svg></div></div>
    <div class="pkg-row"><div class="feature">Paperwork health check</div><div class="mark"><svg><use href="#tick"/></svg></div><div class="mark"><svg><use href="#tick"/></svg></div><div class="mark"><svg><use href="#tick"/></svg></div><div class="mark"><svg><use href="#tick"/></svg></div></div>
    <div class="pkg-row"><div class="feature">Full sales management</div><div class="mark"><svg><use href="#tick"/></svg></div><div class="mark"><svg><use href="#tick"/></svg></div><div class="mark"><svg><use href="#tick"/></svg></div><div class="mark"><svg><use href="#tick"/></svg></div></div>
    <div class="pkg-row"><div class="feature">Dedicated Account Manager</div><div class="mark"><svg><use href="#tick"/></svg></div><div class="mark"><svg><use href="#tick"/></svg></div><div class="mark"><svg><use href="#tick"/></svg></div><div class="mark"><svg><use href="#tick"/></svg></div></div>
    <div class="pkg-row"><div class="feature">Contract with The Brivo Agent</div><div class="mark"><svg><use href="#tick"/></svg></div><div class="mark"><svg><use href="#tick"/></svg></div><div class="mark"><svg><use href="#tick"/></svg></div><div class="mark"><svg><use href="#tick"/></svg></div></div>
    <div class="pkg-row"><div class="feature">24hr Selling</div><div class="mark"><svg><use href="#tick"/></svg></div><div class="mark"><svg><use href="#tick"/></svg></div><div class="mark"><svg><use href="#tick"/></svg></div><div class="mark"><svg><use href="#tick"/></svg></div></div>
    <div class="pkg-row"><div class="feature">Advertising in Spanish media</div><div class="mark"><svg><use href="#tick"/></svg></div><div class="mark"><svg><use href="#tick"/></svg></div><div class="mark"><svg><use href="#tick"/></svg></div><div class="mark"><svg><use href="#tick"/></svg></div></div>
    <div class="pkg-row"><div class="feature">Viewing statistics</div><div class="mark"><svg><use href="#tick"/></svg></div><div class="mark"><svg><use href="#tick"/></svg></div><div class="mark"><svg><use href="#tick"/></svg></div><div class="mark"><svg><use href="#tick"/></svg></div></div>
    <div class="pkg-row"><div class="feature">Introduction to your personal legal advisor</div><div class="mark"><svg><use href="#tick"/></svg></div><div class="mark"><svg><use href="#tick"/></svg></div><div class="mark"><svg><use href="#tick"/></svg></div><div class="mark"><svg><use href="#tick"/></svg></div></div>
    <div class="pkg-row"><div class="feature">Loading property to sites</div><div class="mark"><svg><use href="#tick"/></svg></div><div class="mark"><svg><use href="#tick"/></svg></div><div class="mark"><svg><use href="#tick"/></svg></div><div class="mark"><svg><use href="#tick"/></svg></div></div>
    <div class="pkg-row"><div class="feature">Advertise on major portals</div><div class="mark"><svg><use href="#tick"/></svg></div><div class="mark"><svg><use href="#tick"/></svg></div><div class="mark"><svg><use href="#tick"/></svg></div><div class="mark"><svg><use href="#tick"/></svg></div></div>
    <div class="pkg-row"><div class="feature">Including Casaview</div><div class="mark"><svg><use href="#cross"/></svg></div><div class="mark"><svg><use href="#tick"/></svg></div><div class="mark"><svg><use href="#tick"/></svg></div><div class="mark"><svg><use href="#tick"/></svg></div></div>
    <div class="pkg-row"><div class="feature">Photography</div><div class="mark"><svg><use href="#cross"/></svg></div><div class="mark"><svg><use href="#tick"/></svg></div><div class="mark"><svg><use href="#tick"/></svg></div><div class="mark"><svg><use href="#tick"/></svg></div></div>
    <div class="pkg-row"><div class="feature">Copy writing</div><div class="mark"><svg><use href="#cross"/></svg></div><div class="mark"><svg><use href="#tick"/></svg></div><div class="mark"><svg><use href="#tick"/></svg></div><div class="mark"><svg><use href="#tick"/></svg></div></div>
    <div class="pkg-row"><div class="feature">Internal video</div><div class="mark"><svg><use href="#cross"/></svg></div><div class="mark"><svg><use href="#tick"/></svg></div><div class="mark"><svg><use href="#tick"/></svg></div><div class="mark"><svg><use href="#tick"/></svg></div></div>
    <div class="pkg-row"><div class="feature">Floor plan</div><div class="mark"><svg><use href="#cross"/></svg></div><div class="mark"><svg><use href="#cross"/></svg></div><div class="mark"><svg><use href="#tick"/></svg></div><div class="mark"><svg><use href="#tick"/></svg></div></div>
    <div class="pkg-row"><div class="feature">Drone aerial footage X X</div><div class="mark"><svg><use href="#cross"/></svg></div><div class="mark"><svg><use href="#cross"/></svg></div><div class="mark"><svg><use href="#tick"/></svg></div><div class="mark"><svg><use href="#tick"/></svg></div></div>
    <div class="pkg-row"><div class="feature">Home staging consultation X X</div><div class="mark"><svg><use href="#cross"/></svg></div><div class="mark"><svg><use href="#cross"/></svg></div><div class="mark"><svg><use href="#tick"/></svg></div><div class="mark"><svg><use href="#tick"/></svg></div></div>
    <div class="pkg-row"><div class="feature">Premium Listing X X X</div><div class="mark"><svg><use href="#cross"/></svg></div><div class="mark"><svg><use href="#cross"/></svg></div><div class="mark"><svg><use href="#cross"/></svg></div><div class="mark"><svg><use href="#tick"/></svg></div></div>
    <div class="pkg-row price-row"><div class="feature">Price</div><div class="price">€399</div><div class="price">€499</div><div class="price">€599</div><div class="price">€699</div></div>
    <div class="pkg-row offer-row"><div class="feature">Launch offer</div><div class="price">€299</div><div class="price">€399</div><div class="price">€499</div><div class="price">€599</div></div>
  </section>

  <footer class="footer">
    <p>Our agents are on hand to help, so call now on +34 900 555 014 / 600 555 218 to discuss the best package for you.</p>
    <p>Or visit our website for more details: <span class="site">www.thebrivoagency.com</span></p>
  </footer>
</div>
</body>
</html>
```